Brisk Lantern Accounting - New client package

I need a stationary package (presentation folder cover, welcome letter template/design, sample financial report template/design, business card and new logo) for my accounting business. I would like to see designs that use the color blue. Financial icons can be included in the design. The final design should be clean and communicate professionalism and the use of modern; user-friendly technology. Attached postcard files should help with overall design concept.

```html
<!DOCTYPE html>
<html lang="en">
<head>
<meta charset="utf-8">
<title>Brisk Lantern Accounting – Presentation Folder</title>
<link href="https://fonts.googleapis.com/css2?family=Montserrat:wght@300;400;500;600&display=swap" rel="stylesheet">
<style>
  :root {
    --backdrop: #e4e5e7;
    --paper: #ffffff;
    --navy: #0d4a8f;
    --blue: #1f7fc0;
    --ink: #3a3f45;
    --photo-deep: #0b3f6e;
    --photo-mid: #2f7fb5;
    --photo-light: #a9d3ec;
  }
  * { box-sizing: border-box; margin: 0; padding: 0; }
  html, body {
    width: 1200px; height: 854px; overflow: hidden;
    background: var(--backdrop);
    font-family: "Montserrat", sans-serif;
  }
  .folder-spread {
    position: absolute; left: 150px; top: 127px;
    width: 900px; height: 600px;
    display: flex;
    box-shadow: 0 6px 24px rgba(0,0,0,.12);
  }
  .panel { position: relative; width: 450px; height: 600px; background: var(--paper); overflow: hidden; }
  .panel--back { border-right: 1px solid rgba(0,0,0,.06); }

  .cover-photo {
    position: absolute; top: 0; height: 600px;
    background:
      linear-gradient(100deg, transparent 40%, rgba(169,211,236,.85) 48%, rgba(169,211,236,.85) 52%, transparent 60%),
      linear-gradient(180deg, var(--photo-mid) 0%, var(--photo-deep) 100%);
  }
  .panel--back .cover-photo { left: 190px; width: 260px; background-size: 710px 600px; background-position: 0 0; }
  .panel--front .cover-photo { left: 0; width: 360px; background-size: 710px 600px; background-position: -260px 0; }

  .brand-lockup {
    position: absolute; left: 30px; top: 64px;
    display: flex; align-items: center; gap: 10px;
  }
  .brand-lockup__mark { width: 12px; height: 12px; background: var(--blue); }
  .brand-lockup__name {
    color: var(--navy); font-weight: 400; font-size: 11px;
    letter-spacing: .08em; line-height: 1.15; text-transform: uppercase;
  }

  .contact-block {
    position: absolute; left: 32px; bottom: 34px;
    color: var(--ink); font-size: 7.5px; line-height: 1.45;
  }
  .contact-block__address { margin-bottom: 8px; }
  .contact-line { display: flex; align-items: center; gap: 6px; }
  .contact-line svg { width: 7px; height: 7px; fill: var(--blue); }

  .front-badge {
    position: absolute; right: 28px; top: 66px;
    width: 150px; height: 68px; background: var(--paper);
    display: flex; align-items: center; justify-content: center;
  }
  .front-badge__name {
    color: var(--navy); font-weight: 500; font-size: 17px;
    letter-spacing: .04em; text-transform: uppercase;
  }

  .front-title {
    position: absolute; right: 22px; bottom: 70px;
    transform-origin: right bottom;
    transform: rotate(-90deg) translateX(100%);
    color: var(--navy); font-weight: 400; font-size: 24px;
    line-height: 1.05; letter-spacing: .04em; text-transform: uppercase;
    white-space: nowrap;
  }
</style>
</head>
<body>
  <main class="folder-spread">
    <section class="panel panel--back">
      <div class="brand-lockup">
        <span class="brand-lockup__mark"></span>
        <span class="brand-lockup__name">Brisk Lantern<br>Accounting</span>
      </div>
      <div class="cover-photo" role="img" aria-label="Upward view of blue glass office towers against a pale sky"></div>
      <address class="contact-block">
        <p class="contact-block__address">Level 12, Harbour House<br>18 Quay Lane, Sydney</p>
        <p class="contact-line"><svg viewBox="0 0 10 10"><path d="M2 0h2l1 3-1.5 1a6 6 0 0 0 2.5 2.5L7 5l3 1v2a2 2 0 0 1-2 2A8 8 0 0 1 0 2a2 2 0 0 1 2-2z"/></svg>305-555-0147</p>
        <p class="contact-line"><svg viewBox="0 0 10 10"><path d="M0 2h10v6H0z M0 2l5 3.5L10 2" fill="none" stroke="#1f7fc0" stroke-width="1"/></svg>info@brisklanternaccounting.com</p>
        <p class="contact-line"><svg viewBox="0 0 10 10"><circle cx="5" cy="5" r="4.3" fill="none" stroke="#1f7fc0"/><path d="M.7 5h8.6M5 .7c-2.5 2.8-2.5 5.8 0 8.6M5 .7c2.5 2.8 2.5 5.8 0 8.6" fill="none" stroke="#1f7fc0" stroke-width=".8"/></svg>www.brisklanternaccounting.com</p>
      </address>
    </section>
    <section class="panel panel--front">
      <div class="cover-photo" role="img" aria-label="Upward view of blue glass office towers against a pale sky"></div>
      <div class="front-badge"><span class="front-badge__name">Brisk Lantern</span></div>
      <h1 class="front-title">Brisk Lantern<br>Accounting</h1>
    </section>
  </main>
</body>
</html>
```